依頼詳細
■サブタイトル
*添付のPDFの見本(以下PDF)は英語ですが日本語(カタカナ)に変えてもOK
*適当な文章に変えてもOK
*サブタイトルは無くてもOK

■タイトル
*PDFは「Lumo7,inc.」ですが「ルモセブン」でもOK
*PDFの書体でなく変えてもOK
*位置は左側でなく、現在のHPのように左右センターでもOK

■タイトル右側の空白部分
*可能ならイメージカットを入れるかデザイン処理を希望
*ごちゃごちゃするようなら、空白のままでOK

■上ナビ
*入れる文字はPDF同様の項目を使用
(必要に応じてデザイン処理を希望)

■トップページ本文
*PDFは横に4つのレイアウトですが変えてもOK
*イメージ画像はできるだけ指定通りの大きさで
(スマホ時に縦の長さを短くしたいため)
*イメージ画像は写真でもイラストでもOK
(使用例は添付ファイル参照)
*各ブロックの「詳しくはこちらをご覧ください。」は画像処理でもOK
(文章を変えてもOK)

■サブページ本文
*一部に画像を使用するか、小見出しのデザイン処理を希望

■フッター
*PDFはフッターの天地が狭く、ページ全体が横長で収まりが悪いので天地は多少広めが希望
*バランス的に問題なければ自社メディアの紹介も希望
(バナーでなくテキスト一覧が希望。サイト名は添付ファイル参照)
サイトURL
http://www.lumo7.co.jp/
ページ数
2ページ
希望イメージ
シンプル 複雑
単色 カラフル
暗い 明るい
日常 高級
遊び心 厳粛
未来的 伝統的
女性的 男性的
希望する色
色はお任せします。(基本は落ち着いた感じの色合いでお願いします)
納品ファイル
• フォトショップ形式 (.psd)
• PNG形式 (.png)
補足説明
※納品ファイルはフォトショップ形式がなければPNG形式のみでもかまいません。

★締切日当日のご提案は、採用候補でも修正依頼が出せないため、気に入った案でも候補に入れられないので、できるだけ初回のご提案は締切日の2~3日前までにいただけましたら幸いです。
メインに大きい写真を使用していただくご提案の場合は、4つのイメージ画像も写真にすると色が多すぎてしまう感じがするので、4つのイメージ画像は(多色でない)イラストにするとか、カラー写真を使用しないなどを希望します。

また、主なWEBメディア一覧を入れていただくご提案の場合は、トップページのフッターのみに入れて、サブページは不要とさせてください。
こちらを入れる目的はトップページから各サイトに被リンクを与えることですので、全ページに掲載すると逆に被リンクが多すぎてSEO的に問題があるためです。
したがって、各サイトへの誘導が目的ではありませんのでこの部分は特に目立たせる必要はなく、フッターに入れていただく場合は、さり気なくバランスよく入る場合のみでかまいません。

いろいろと希望が多くて申し訳ございませんが、よろしくお願いいたします。

全体のバランスがよくや色使いも落ち着いていて好みだったので、決めさせていただきました。
また、修正依頼などもすぐに対応いただき、助かりました。

多くのご提案をいただき、ありがとうございました。
結局は主観的な好みで決めさせていただきましたが、かなり迷ったご提案も数点ありました。
なお、締切日ギリギリのご提案は、修正依頼が出せないので、良いご提案も見送らせていただいたものもありました。

```html
<!DOCTYPE html>
<html lang="ja">
<head>
<meta charset="utf-8">
<title>Lumo7,inc. ルモセブン</title>
<link href="https://fonts.googleapis.com/css2?family=Noto+Sans+JP:wght@400;700;900&display=swap" rel="stylesheet">
<style>
:root{
  --red:#d7141a;
  --red-dark:#a80e12;
  --ink:#333;
  --muted:#666;
  --page:#e9e9e9;
  --card:#fff;
  --bar:#2e2e2e;
  --footer:#3b3b3b;
  --bottom:#111;
}
*{box-sizing:border-box;margin:0;padding:0}
html,body{width:867px;height:1200px;overflow:hidden}
body{font-family:"Noto Sans JP",sans-serif;color:var(--ink);background:var(--page);font-size:12px;position:relative}
.site-header{height:110px;background:#fff;position:relative;padding:10px 23px}
.tagline{font-size:11px;color:var(--muted);letter-spacing:.05em}
.brand{display:flex;align-items:center;gap:10px;margin-top:10px;color:var(--red);font-weight:900;font-size:30px;line-height:1}
.brand .kana{font-size:22px}
.contact-btn{position:absolute;right:23px;top:14px;background:var(--red);color:#fff;font-size:12px;font-weight:700;padding:6px 14px;border-radius:3px;display:flex;align-items:center;gap:6px}
.global-nav{height:35px;background:linear-gradient(var(--red),var(--red-dark));display:flex;padding:0 23px}
.global-nav a,.footer-nav a{flex:1;color:#fff;text-decoration:none;font-weight:700;font-size:12px;display:flex;align-items:center;justify-content:center;border-right:1px solid rgba(255,255,255,.35)}
.global-nav a:last-child,.footer-nav a:last-child{border-right:none}
.hero{height:265px;background:linear-gradient(120deg,#f4f4f4 0%,#d9d9d9 45%,#7a7a7a 60%,#e8e8e8 80%,#cfcfcf 100%)}
.services{position:relative;display:flex;gap:15px;padding:0 23px;height:600px;margin-top:-35px}
.service{flex:1;background:var(--card);display:flex;flex-direction:column;box-shadow:0 1px 3px rgba(0,0,0,.15)}
.service-image{height:160px}
.img-marketing{background:linear-gradient(135deg,#cfe6ee,#6fa9c4 60%,#2f6b8a)}
.img-ads{background:linear-gradient(135deg,#f2f2f2,#b9b9b9 50%,#c0392b)}
.img-media{background:linear-gradient(135deg,#dfeccb,#7fa64e 55%,#3f5e25)}
.img-direct{background:linear-gradient(135deg,#9a9a9a,#4a4a4a 55%,#1e1e1e)}
.service h2{background:var(--bar);color:#fff;font-size:13px;text-align:center;height:28px;line-height:28px;font-weight:700}
.service p{padding:12px 12px 0;font-size:11px;line-height:1.75;color:#444;flex:1}
.more-btn{margin:0 12px 18px;height:30px;background:linear-gradient(var(--red),var(--red-dark));color:#fff;font-weight:700;font-size:12px;display:flex;align-items:center;justify-content:center;gap:8px;border-radius:2px}
.media-list{position:absolute;top:985px;left:0;width:867px;height:140px;background:var(--footer);color:#ddd;padding:16px 40px 0}
.media-list h3{text-align:center;font-size:13px;color:#fff;font-weight:700;margin-bottom:12px}
.media-list ul{list-style:none;display:grid;grid-template-columns:repeat(4,1fr);row-gap:10px;font-size:11px}
.media-list li::before{content:"▶";color:#bbb;font-size:8px;margin-right:6px;vertical-align:1px}
.footer-nav{position:absolute;top:1125px;left:0;width:867px;height:24px;background:var(--red);display:flex;padding:0 23px}
.bottom-bar{position:absolute;top:1149px;left:0;width:867px;height:51px;background:var(--bottom);color:#bbb;text-align:center;font-size:11px;padding-top:8px}
.bottom-links span{margin:0 8px}
.copyright{margin-top:6px;font-size:10px;color:#888}
</style>
</head>
<body>
<header class="site-header">
  <p class="tagline">Web marketing &amp; Direct marketing Service</p>
  <div class="brand"><span>Lumo7,inc.</span><span class="kana">ルモセブン</span></div>
  <div class="contact-btn">
    <svg width="12" height="10" viewBox="0 0 12 10"><rect x="0.5" y="0.5" width="11" height="9" fill="none" stroke="#fff"/><path d="M0.5 0.5 6 5.5 11.5 0.5" fill="none" stroke="#fff"/></svg>
    お問い合わせ
  </div>
</header>
<nav class="global-nav">
  <a href="#">TOP</a><a href="#">WEBマーケティング</a><a href="#">WEB広告</a><a href="#">WEBメディア</a><a href="#">ダイレクトマーケティング</a>
</nav>
<div class="hero" role="img" aria-label="机の上に置かれたスマートフォンとノートパソコンの写真"></div>
<main class="services">
  <section class="service">
    <div class="service-image img-marketing" role="img" aria-label="マーケティングを表すイラスト"></div>
    <h2>WEBマーケティング</h2>
    <p>お客様のニーズを調査して、ターゲットに最適なWEBマーケティング手法をご提案いたします。集客から分析、改善までを一貫してサポートし、SEO対策やコンテンツ制作を通じて、継続的に成果を生み出すサイト運営をお手伝いいたします。</p>
    <div class="more-btn">詳細はこちら <span>›</span></div>
  </section>
  <section class="service">
    <div class="service-image img-ads" role="img" aria-label="広告を表すイラスト"></div>
    <h2>WEB広告</h2>
    <p>お客様のご要望をお伺いして、効果的なWEB広告の運用を行います。リスティング広告やSNS広告、ディスプレイ広告など、目的に合わせた媒体を選定し、費用対効果の高い広告展開をご提案いたします。</p>
    <div class="more-btn">詳細はこちら <span>›</span></div>
  </section>
  <section class="service">
    <div class="service-image img-media" role="img" aria-label="メディア運営を表すイラスト"></div>
    <h2>WEBメディア</h2>
    <p>当社では、WEBマーケティングのノウハウを活かして自社WEBメディアを運営しております。生活に役立つ情報から専門分野まで、幅広いジャンルのポータルサイトを展開し、多くの方にご利用いただいております。</p>
    <div class="more-btn">詳細はこちら <span>›</span></div>
  </section>
  <section class="service">
    <div class="service-image img-direct" role="img" aria-label="ダイレクトマーケティングを表すイラスト"></div>
    <h2>ダイレクトマーケティング</h2>
    <p>ユーザーに直接届くダイレクトマーケティングで、ニーズに合わせた情報を効果的に発信します。メール配信やDM、電話によるご案内まで、お客様の販売促進をトータルでサポートいたします。</p>
    <div class="more-btn">詳細はこちら <span>›</span></div>
  </section>
</main>
<footer>
  <div class="media-list">
    <h3>主なWEBメディア一覧</h3>
    <ul>
      <li>ルモ住まいナビ</li><li>ひなた暮らし便</li><li>キャンパス寮ルーム</li><li>みらい住まい館</li>
      <li>グローバル留学ポート</li><li>はじめての社会人帖</li><li>ルモ広告ラボ</li><li>まなびの森</li>
      <li>くらし修理ノート</li><li>あおぞら賃貸</li><li>通学ルーム検索</li><li>さくら女子寮ナビ</li>
    </ul>
  </div>
  <nav class="footer-nav">
    <a href="#">TOP</a><a href="#">WEBマーケティング</a><a href="#">WEB広告</a><a href="#">WEBメディア</a><a href="#">ダイレクトマーケティング</a>
  </nav>
  <div class="bottom-bar">
    <div class="bottom-links"><span>会社概要</span>|<span>プライバシーポリシー</span>|<span>サイトマップ</span>|<span>お問い合わせ</span></div>
    <div class="copyright">Copyright © Lumo7,inc. All Rights Reserved.</div>
  </div>
</footer>
</body>
</html>
```